Pharmacy

Two sided postcard. Pictures on one side. Description on the other. We design and build pharmacies. pictures are some of our finished work. You can use as many pictures as you like not necessary to use all of them. Size of card should be 5"x7". See my website at display@brightfieldfixtures.com for more inspiration. I include the back of one card that I used recently. Both sids need design input. Feel free to contact me with questions.
Requirements
Must have
- Must be a two sided postcard
Nice to have
- I am sending a design of a sleek type postcard that I saw online as an example.
- https://lnk.example-pics.net/images/q7KmRz
- I am looking for something modern.
- Not limited to colors on my website.

```html
<!DOCTYPE html>
<html lang="en">
<head>
<meta charset="utf-8">
<title>Brightfield Fixtures &amp; Display – Postcard</title>
<link rel="stylesheet" href="https://fonts.googleapis.com/css2?family=Montserrat:ital,wght@0,400;0,500;0,600;0,700;0,800;0,900;1,700;1,800&display=swap">
<style>
  :root {
    --red: #b1282f;
    --navy: #363b4b;
    --charcoal: #333335;
    --ink: #2c2f3a;
    --paper: #ffffff;
    --stage: #e4e4e4;
    --stamp: #ececec;
    --seam: #4b4b4d;
  }
  * { box-sizing: border-box; margin: 0; padding: 0; }
  html, body { width: 1200px; height: 1200px; overflow: hidden; }
  body {
    background: var(--stage);
    font-family: "Montserrat", Arial, sans-serif;
    color: var(--ink);
    position: relative;
  }
  .postcard-set {
    position: absolute;
    left: 235px; top: 76px;
    width: 912px; height: 1310px;
    transform: scale(0.8);
    transform-origin: top left;
  }
  .side { position: absolute; left: 0; width: 912px; height: 650px; background: var(--paper); overflow: hidden; }
  .side--front { top: 0; }
  .side--back { top: 660px; }
  .seam { position: absolute; left: 0; top: 650px; width: 912px; height: 10px; background: var(--seam); }

  /* Front */
  .front-navy { position: absolute; right: 0; top: 0; width: 642px; height: 565px; background: var(--navy); }
  .front-stripe { position: absolute; left: 0; top: 0; }
  .hero-photo {
    position: absolute; left: 44px; top: 44px; width: 824px; height: 524px;
    border-radius: 24px;
    background: linear-gradient(120deg, #5a5048 0%, #2e2824 40%, #6b6158 70%, #d9d6d0 100%);
  }
  .front-wedge { position: absolute; left: 0; top: 0; }
  .front-title {
    position: absolute; left: 44px; top: 82px; width: 280px;
    font-weight: 900; font-size: 29.5px; line-height: 33px; color: var(--paper);
    text-transform: uppercase; letter-spacing: 0.2px;
  }
  .front-rule { position: absolute; left: 44px; top: 220px; width: 209px; height: 2px; background: var(--paper); }
  .front-tagline {
    position: absolute; left: 44px; top: 229px; width: 220px;
    font-weight: 800; font-style: italic; font-size: 17px; line-height: 22px; color: var(--paper);
  }
  .thumb-strip { position: absolute; left: 123px; top: 425px; width: 683px; height: 143px; background: var(--paper); }
  .thumb { position: absolute; top: 9px; width: 157px; height: 124px; }
  .thumb--1 { left: 11px; background: linear-gradient(135deg, #7a4a33, #c9a27a 50%, #5e3d2b); }
  .thumb--2 { left: 179px; background: linear-gradient(160deg, #b8a58c, #8a6a4e 45%, #e9e4dc 70%, #2b2b2b); }
  .thumb--3 { left: 347px; background: linear-gradient(150deg, #6b4a3a, #d8cfc2 50%, #7c5a43); }
  .thumb--4 { left: 515px; background: linear-gradient(120deg, #c44a3a, #e8e2da 45%, #a8c3c9 80%); }
  .front-contact {
    position: absolute; left: 44px; top: 590px; width: 824px;
    display: flex; justify-content: space-between; align-items: center;
    font-weight: 600; font-size: 17px; white-space: nowrap;
  }
  .contact-item { display: flex; align-items: center; gap: 6px; }
  .contact-item svg { width: 20px; height: 20px; flex: none; }
  .accent { color: var(--red); }

  /* Back */
  .back-panel { position: absolute; left: 0; top: 0; width: 457px; height: 650px; background: var(--red); }
  .back-title {
    position: absolute; left: 44px; top: 50px; width: 410px;
    font-weight: 800; font-size: 29.5px; line-height: 35px; color: var(--paper); text-transform: uppercase;
  }
  .back-band { position: absolute; left: 0; top: 125px; width: 457px; height: 38px; background: var(--charcoal); }
  .back-tagline {
    position: absolute; left: 44px; top: 129px;
    font-weight: 800; font-style: italic; font-size: 22px; color: var(--paper);
  }
  .about-box { position: absolute; left: 0; top: 163px; width: 457px; height: 210px; background: var(--paper); }
  .about-text {
    position: absolute; left: 44px; top: 170px; width: 396px;
    font-size: 17.6px; line-height: 23.5px; text-align: justify; color: var(--ink); font-weight: 400;
  }
  .back-photo { position: absolute; top: 373px; height: 123px; }
  .back-photo--aisle { left: 0; width: 212px; background: linear-gradient(135deg, #d9d4cc, #7a6a58 50%, #394a6b); }
  .back-photo--counter { left: 224px; width: 233px; background: linear-gradient(160deg, #5a4a3e, #e6ddd0 55%, #c9b89e); }
  .back-photo-gap { position: absolute; left: 212px; top: 373px; width: 12px; height: 123px; background: var(--paper); }
  .call-band { position: absolute; left: 0; top: 508px; width: 457px; height: 48px; background: var(--charcoal); }
  .call-label {
    position: absolute; left: 44px; top: 516px; width: 86px;
    font-weight: 700; font-size: 14px; line-height: 15px; color: var(--paper); text-align: right;
  }
  .call-icon { position: absolute; left: 138px; top: 512px; width: 40px; height: 40px; }
  .call-number { position: absolute; left: 187px; top: 508px; font-weight: 800; font-size: 36.5px; line-height: 48px; color: var(--paper); }
  .back-links {
    position: absolute; left: 46px; top: 565px;
    font-weight: 600; font-size: 18.5px; line-height: 23px; color: var(--paper);
  }
  .back-links .contact-item svg { width: 18px; height: 18px; }

  .return-address { position: absolute; left: 508px; top: 65px; display: flex; gap: 6px; }
  .return-address svg { width: 22px; height: 22px; flex: none; margin-top: -2px; }
  .return-address p { font-size: 14px; line-height: 17px; color: var(--ink); }
  .return-address strong { font-weight: 700; }
  .postage-box {
    position: absolute; left: 745px; top: 20px; width: 149px; height: 165px; background: var(--stamp);
    display: flex; align-items: center; justify-content: center; text-align: center;
    font-size: 14.5px; line-height: 17.5px; color: #444;
  }
</style>
</head>
<body>
<main class="postcard-set">

  <section class="side side--front" aria-label="Postcard front">
    <div class="front-navy"></div>
    <svg class="front-stripe" width="912" height="60" viewBox="0 0 912 60"><polygon points="225,0 272,0 290,42 252,42" fill="#ffffff"/></svg>
    <div class="hero-photo" role="img" aria-label="Photo of a finished cosmetics counter with dark wood shelving stocked with products"></div>
    <svg class="front-wedge" width="360" height="460" viewBox="0 0 360 460">
      <path d="M0,0 L225,0 L335,152 Q342,168 328,182 L0,455 Z" fill="#b1282f"/>
    </svg>
    <h1 class="front-title">Brightfield Fixtures &amp; Display Co. Inc.</h1>
    <div class="front-rule"></div>
    <p class="front-tagline">A Complete Service From Design Thru Installation</p>

    <div class="thumb-strip">
      <div class="thumb thumb--1" role="img" aria-label="Photo of pharmacy wall shelving"></div>
      <div class="thumb thumb--2" role="img" aria-label="Photo of pharmacy checkout counter"></div>
      <div class="thumb thumb--3" role="img" aria-label="Photo of glass display showcase"></div>
      <div class="thumb thumb--4" role="img" aria-label="Photo of pharmacy retail aisle"></div>
    </div>

    <div class="front-contact">
      <span class="contact-item accent">
        <svg viewBox="0 0 20 20"><circle cx="10" cy="10" r="8.5" fill="none" stroke="#2c2f3a" stroke-width="1.4"/><path d="M7 5.5l2 2-1 1.3c.6 1.3 1.6 2.3 2.9 2.9l1.3-1 2 2-1.3 1.3c-3.3-.4-6.4-3.5-6.8-6.8z" fill="#b1282f"/></svg>
        201 555 0148
      </span>
      <span class="contact-item">
        <svg viewBox="0 0 20 20"><circle cx="10" cy="10" r="8.5" fill="none" stroke="#2c2f3a" stroke-width="1.4"/><rect x="5.5" y="7" width="9" height="6.5" fill="none" stroke="#b1282f" stroke-width="1.3"/><path d="M5.5 7l4.5 3.5 4.5-3.5" fill="none" stroke="#b1282f" stroke-width="1.3"/></svg>
        display@brightfieldfixtures.com
      </span>
      <span class="contact-item">
        <svg viewBox="0 0 20 20"><circle cx="10" cy="10" r="8.5" fill="none" stroke="#2c2f3a" stroke-width="1.4"/><circle cx="10" cy="10" r="4.5" fill="none" stroke="#b1282f" stroke-width="1.3"/><path d="M5.5 10h9M10 5.5v9" stroke="#b1282f" stroke-width="1"/></svg>
        <span>www.<span class="accent">brightfieldfixtures</span>.com</span>
      </span>
    </div>
  </section>

  <div class="seam"></div>

  <section class="side side--back" aria-label="Postcard back">
    <div class="back-panel"></div>
    <h2 class="back-title">Brightfield Fixtures &amp; Display Co. Inc.</h2>
    <div class="back-band"></div>
    <p class="back-tagline">Quality - Experience - Innovation</p>
    <div class="about-box"></div>
    <p class="about-text">Family owned and operated for three generations -Brightfield Fixtures &amp; Display Co. Inc is the oldest store fixture company in New Jersey. As designers &amp; Manufacturers we can save you hours of time and money. Our level of experience will be evident from the outset and you will be pleased that you found us.</p>
    <div class="back-photo back-photo--aisle" role="img" aria-label="Photo of pharmacy aisle with product gondolas"></div>
    <div class="back-photo-gap"></div>
    <div class="back-photo back-photo--counter" role="img" aria-label="Photo of pharmacy counter with pendant lights"></div>

    <div class="call-band"></div>
    <p class="call-label">GIVE US A CALL AT</p>
    <svg class="call-icon" viewBox="0 0 40 40"><circle cx="20" cy="20" r="17.5" fill="none" stroke="#ffffff" stroke-width="2"/><path d="M13 11l4.5 4.5-2 2.6c1.3 2.8 3.4 4.9 6.2 6.2l2.6-2 4.5 4.5-2.8 2.8C19 29 11 21 10.2 13.8z" fill="#b1282f"/></svg>
    <p class="call-number">201 555 0148</p>

    <div class="back-links">
      <div class="contact-item">
        <svg viewBox="0 0 20 20"><circle cx="10" cy="10" r="8.5" fill="none" stroke="#ffffff" stroke-width="1.4"/><rect x="5.5" y="7" width="9" height="6.5" fill="none" stroke="#ffffff" stroke-width="1.3"/><path d="M5.5 7l4.5 3.5 4.5-3.5" fill="none" stroke="#ffffff" stroke-width="1.3"/></svg>
        display@brightfieldfixtures.com
      </div>
      <div class="contact-item">
        <svg viewBox="0 0 20 20"><circle cx="10" cy="10" r="8.5" fill="none" stroke="#ffffff" stroke-width="1.4"/><circle cx="10" cy="10" r="4.5" fill="none" stroke="#ffffff" stroke-width="1.3"/><path d="M5.5 10h9M10 5.5v9" stroke="#ffffff" stroke-width="1"/></svg>
        www.brightfieldfixtures.com
      </div>
    </div>

    <div class="return-address">
      <svg viewBox="0 0 22 22"><circle cx="11" cy="11" r="9.5" fill="none" stroke="#2c2f3a" stroke-width="1.4"/><path d="M6 11l5-4.5 5 4.5v4.5H6z" fill="#b1282f"/></svg>
      <p><strong>Brightfield Fixtures &amp;<br>Display Co. Inc.</strong><br>PO Box 318<br>Ridgeford NJ 07690</p>
    </div>
    <div class="postage-box"><p>presorted<br>FIRST CLASS<br>US POSTAGE<br>PAID<br>Postline</p></div>
  </section>

</main>
</body>
</html>
```